Condo Debts Collection Business needs a Web Design (Contest)

I need a site for a client, who works with condo debts collection, and ensure all revenues provided by condo fees will be always available to the building manager of condo on a specific date, regardless of defaults.I have the logo of the companies, and some requirements on layout (kind of slider, menu options, phone number on a noble position, etc).
Updates

Designs look the same

Target Market(s)

I have two targets for this design: - Condominium's building manager. This target is looking for a solution to overdue debts on it's condo. - Residents on condominiums. This target wants to live in a better place, where their neighbors pay their condominium fees on time.

Number of Pages Required

1 page

Requirements
Must have
• - Slider with title, some short text related, a nice image (I prefer happy and/or peaceful family, people doing business, happy friends, and so on).
• - I have a special attention to menu. I'm looking for one I can have a nice effect, more elegant, charming, kind of innovative.
• - Phone number on the top (or clearly visible).
• - Member log in area or icon on the top (or clearly visible).
• - News/articles area.
• - Modern fonts, with good quality, sans-serif on areas where reading is more intensive (prefer Google web-fonts).
• - Colors specified on attached files.
• - Header similar or inspired by the "FILE 3"
Nice to have
• - Clear background color, cause it's better to read larger texts (like articles). Dark backgrounds makes reading difficult.
• - A site with effects (like shadows, lines, gradients, lights) is usually pretty.
• - I pay attention on beautiful footers.
Should not have
• - Images with a lot of money (I don't sell richness, I sell tranquility, peace, harmony, safety).
• - Poor menu.
• - Lots of curves. My customer asked for straight lines.

```html
<!DOCTYPE html>
<html lang="pt">
<head>
<meta charset="utf-8">
<title>Serencasa — Cobrança Condominial</title>
<link rel="stylesheet" href="https://fonts.googleapis.com/css2?family=Montserrat:wght@400;500;600;700&display=swap">
<style>
  :root {
    --navy: #0b3a73;
    --navy-deep: #082f60;
    --orange: #e57b1b;
    --white: #ffffff;
    --footer-blue: #0b4a96;
    --text-blue: #133d74;
  }
  * { box-sizing: border-box; margin: 0; padding: 0; }
  html, body { width: 1200px; height: 1200px; overflow: hidden; }
  body { font-family: "Montserrat", sans-serif; background: var(--white); position: relative; }

  .site-header {
    position: absolute; left: 0; top: 0; width: 1200px; height: 112px;
    background: radial-gradient(ellipse at 15% 40%, #14498a 0%, var(--navy) 45%, var(--navy-deep) 100%);
  }
  .brand {
    position: absolute; left: 48px; top: 38px;
    display: flex; align-items: center; gap: 12px;
    color: var(--white); font-weight: 700; font-size: 24px; letter-spacing: 0.5px;
  }
  .brand-mark { width: 34px; height: 34px; border-radius: 50%; background: var(--orange); }
  .main-nav { position: absolute; left: 586px; top: 50px; display: flex; gap: 46px; }
  .main-nav a {
    color: var(--white); text-decoration: none; font-size: 12px; font-weight: 600;
    letter-spacing: 2px; position: relative;
  }
  .main-nav a.is-active::after {
    content: ""; position: absolute; left: 4px; top: 21px; width: 31px; height: 3px; background: var(--orange);
  }
  .account-login {
    position: absolute; left: 986px; top: 37px; width: 214px; height: 40px;
    background: var(--orange); clip-path: polygon(0 0, 100% 0, 100% 100%, 8px 100%);
    display: flex; align-items: center; padding-left: 26px; gap: 12px;
    color: var(--white); font-size: 12px; font-weight: 600; letter-spacing: 2px;
  }

  .hero { position: absolute; left: 0; top: 112px; width: 1200px; height: 496px; background: var(--orange); overflow: hidden; }
  .hero-photo {
    position: absolute; inset: 0;
    background: linear-gradient(100deg, #4c3a30 0%, #5d7570 30%, #c7a48a 55%, #a9c2d6 80%, #e3ebf0 100%);
    clip-path: polygon(472px 0, 1200px 0, 1200px 496px, 374px 496px);
  }
  .hero-title {
    position: absolute; left: 93px; top: 96px;
    color: var(--white); font-weight: 700; font-size: 54px; line-height: 56px; letter-spacing: -1px;
  }
  .hero-lead {
    position: absolute; left: 95px; top: 274px; width: 300px;
    color: var(--navy); font-weight: 700; font-size: 18px; line-height: 23px; letter-spacing: -0.4px;
  }
  .btn {
    position: absolute; display: flex; align-items: center; justify-content: center;
    color: var(--white); font-size: 11.5px; font-weight: 600; letter-spacing: 2px;
  }
  .btn-navy { background: var(--navy); }
  .btn-orange { background: var(--orange); }
  .phone-bar {
    position: absolute; left: 824px; top: 432px; width: 376px; height: 64px;
    background: var(--navy); clip-path: polygon(14px 0, 100% 0, 100% 100%, 0 100%);
    display: flex; align-items: center; padding-left: 52px; gap: 10px;
    color: var(--white); font-size: 22px; font-weight: 700; letter-spacing: -0.3px;
  }

  .intro {
    position: absolute; left: 190px; top: 652px; width: 850px; text-align: center;
    color: var(--navy); font-size: 16px; font-weight: 600; line-height: 24px;
  }
  .divider-shadow {
    position: absolute; left: 140px; top: 740px; width: 960px; height: 20px;
    background: radial-gradient(ellipse at 50% 0%, rgba(11,58,115,0.10) 0%, rgba(11,58,115,0) 70%);
  }

  .about-text { position: absolute; left: 96px; top: 812px; width: 520px; color: var(--text-blue); font-size: 13.6px; line-height: 21.6px; }
  .about-text p + p { margin-top: 22px; }
  .building-photo {
    position: absolute; left: 600px; top: 790px; width: 600px; height: 378px;
    background: linear-gradient(90deg, rgba(255,255,255,1) 0%, rgba(236,240,250,0.6) 22%, rgba(0,0,0,0) 35%),
                linear-gradient(160deg, #e8edf8 0%, #7a4a38 35%, #5b3325 55%, #c8ccd6 75%, #6a9cc4 100%);
  }
  .site-footer { position: absolute; left: 0; top: 1168px; width: 1200px; height: 32px; background: var(--footer-blue); }
</style>
</head>
<body>
  <header class="site-header">
    <div class="brand"><span class="brand-mark"></span>SERENCASA</div>
    <nav class="main-nav">
      <a href="#" class="is-active">HOME</a>
      <a href="#">ABOUT US</a>
      <a href="#">NEWS</a>
      <a href="#">CONTACT</a>
    </nav>
    <a class="account-login" href="#">
      <svg width="13" height="18" viewBox="0 0 13 18" aria-hidden="true"><circle cx="6.5" cy="4.5" r="4" fill="#fff"/><path d="M0 18v-4a5 5 0 0 1 5-5h3a5 5 0 0 1 5 5v4z" fill="#fff"/></svg>
      ACCOUNT LOGIN
    </a>
  </header>

  <section class="hero">
    <div class="hero-photo" role="img" aria-label="Família feliz e tranquila em casa: mãe, pai e filho sorrindo"></div>
    <h1 class="hero-title">Garantindo a<br>tranquilidade do<br>seu condominio</h1>
    <p class="hero-lead">Lorem ipsum dolor sit amet, consectetur adipiscing eiusmod tempor ut dolore magna aliqua.</p>
    <a class="btn btn-navy" href="#" style="left:95px;top:365px;width:168px;height:40px;">FIND OUT MORE</a>
    <div class="phone-bar">
      <svg width="26" height="26" viewBox="0 0 26 26" aria-hidden="true"><circle cx="13" cy="13" r="13" fill="#e57b1b"/><path d="M9 6.5l2.5 3-1.6 1.8c.9 1.9 2.4 3.4 4.3 4.3l1.8-1.6 3 2.5-1.6 2.5c-5.3-.6-9.5-4.8-10.1-10.1z" fill="#0b3a73"/></svg>
      4120-5510 / 4120-5520
    </div>
  </section>

  <p class="intro">Lorem ipsum dolor sit amet, consectetur adipiscing elit, sed do eiusmod tempor incididunt ut labore et dolore magna aliqua. Ut enim ad minim veniam, quis nostrud exercitatio</p>
  <div class="divider-shadow"></div>

  <section class="about-text">
    <p>Lorem ipsum dolor sit amet, consectetur adipiscing elit, sed do eiusmod tempor incididunt ut labore et dolore magna aliqua. Ut enim ad minim veniam, quis nostrud exercitation ullamco laboris nisi ut aliquip ex ea commodo consequat. Duis aute irure dolor in reprehenderit in voluptate velit esse cillum dolore eu fugiat nulla pariatur.</p>
    <p>Sed ut perspiciatis unde omnis iste natus error sit voluptatem accusantium doloremque laudantium, totam rem aperiam, eaque ipsa quae ab illo inventore veritatis et quasi architecto beatae vitae dicta sunt explicabo.</p>
  </section>
  <a class="btn btn-orange" href="#" style="left:96px;top:1045px;width:256px;height:40px;">I AM A BUILDING MANAGER</a>
  <a class="btn btn-orange" href="#" style="left:384px;top:1045px;width:184px;height:40px;">I AM A RESIDENT</a>

  <div class="building-photo" role="img" aria-label="Edifício residencial moderno com varandas de madeira visto de baixo"></div>
  <footer class="site-footer"></footer>
</body>
</html>
```